Business Card- Can you make it cool vs boring!

Need a refresh on my business card! Want it to be modern but simple, classic and a pop of coolness! we do senior living and it is boring. but that doesn't mean our business card have to look boring! Open to two sided cards. our website is www.Tolbera-KM.com

Target Market(s)

capital market

Industry/Entity Type

senior housing/ real estate

Contact Information for Business Card

logo/ name/ cell/ address/ www.Tolbera-KM.com/ space for a QR code

Requirements
Must have
• maybe a QR code (do not make prominent I may not use the QR so design where it can be taken out) that link to more about us/ landing page. needs to be modern but clean
Should not have
• clip art or script

```html
<!DOCTYPE html>
<html lang="en">
<head>
<meta charset="utf-8">
<title>Tolbera Living – Business Card</title>
<link rel="stylesheet" href="https://fonts.googleapis.com/css2?family=Cormorant+Garamond:wght@500;600&family=Roboto:wght@400;500;700&display=swap">
<style>
  :root {
    --backdrop: #d3d3d3;
    --card-white: #ffffff;
    --rust: #b04e24;
    --rust-text: #b5521f;
    --rule: #b8342a;
    --ink: #1c1c1c;
    --ink-soft: #222;
    --social-dot: #151515;
  }
  * { box-sizing: border-box; margin: 0; padding: 0; }
  html, body { width: 1200px; height: 801px; overflow: hidden; }
  body {
    background: var(--backdrop);
    font-family: "Roboto", sans-serif;
    position: relative;
  }
  .card {
    position: absolute;
    top: 252px;
    width: 520px;
    height: 297px;
    border-radius: 22px;
    box-shadow: 0 10px 28px rgba(0,0,0,.22);
    overflow: hidden;
  }
  .card--front { left: 50px; background: var(--card-white); }
  .card--back  { left: 630px; background: var(--rust); }

  /* Front */
  .front-mark {
    position: absolute;
    left: 24px; top: 108px;
    width: 190px;
    text-align: center;
    font-weight: 500;
    font-size: 40px;
    color: var(--rust-text);
  }
  .identity { position: absolute; left: 236px; top: 40px; width: 250px; }
  .identity__name {
    font-family: "Cormorant Garamond", serif;
    font-variant: small-caps;
    font-weight: 600;
    font-size: 30px;
    color: var(--ink);
    line-height: 1;
  }
  .identity__title {
    font-weight: 700;
    font-size: 13px;
    color: var(--rust-text);
    margin-top: 4px;
    letter-spacing: .2px;
  }
  .rule { height: 1px; background: var(--rule); margin: 10px 0; }
  .contact-list { list-style: none; }
  .contact-list li {
    display: flex; align-items: center; gap: 8px;
    font-size: 12.5px; color: var(--ink-soft);
    line-height: 20px;
  }
  .contact-list svg { width: 11px; height: 11px; fill: var(--rust-text); flex: none; }
  .address { font-size: 12.5px; color: var(--ink-soft); line-height: 17px; }
  .tagline {
    position: absolute; left: 236px; right: 20px; bottom: 30px;
    font-weight: 500; font-size: 13px;
    color: var(--rust-text);
    letter-spacing: .3px;
  }

  /* Back */
  .wordmark {
    position: absolute;
    left: 50px; top: 78px;
    color: var(--ink);
    font-weight: 500;
  }
  .wordmark__name {
    font-size: 78px;
    line-height: 1;
    letter-spacing: -1px;
  }
  .wordmark__sub {
    font-size: 22px;
    letter-spacing: 22px;
    margin: 10px 0 0 150px;
    line-height: 1;
  }
  .social {
    position: absolute;
    right: 52px; bottom: 70px;
    display: flex; gap: 8px;
    list-style: none;
  }
  .social li {
    width: 26px; height: 26px;
    border-radius: 50%;
    background: var(--social-dot);
  }
</style>
</head>
<body>
  <section class="card card--front" aria-label="Card front">
    <div class="front-mark">Tolbera</div>
    <div class="identity">
      <h1 class="identity__name">Dan Morrow</h1>
      <p class="identity__title">CHAIRMAN AND CEO</p>
      <div class="rule"></div>
      <ul class="contact-list">
        <li><svg viewBox="0 0 24 24"><path d="M6.6 10.8a15.1 15.1 0 0 0 6.6 6.6l2.2-2.2a1 1 0 0 1 1-.25 11.4 11.4 0 0 0 3.6.6 1 1 0 0 1 1 1V20a1 1 0 0 1-1 1A17 17 0 0 1 3 4a1 1 0 0 1 1-1h3.5a1 1 0 0 1 1 1c0 1.25.2 2.45.6 3.6a1 1 0 0 1-.25 1z"/></svg>(555) 014-2278</li>
        <li><svg viewBox="0 0 24 24"><path d="M2 5h20v14H2z M2 5l10 8 10-8" fill="none" stroke="#b5521f" stroke-width="2.4"/></svg>info@tolbera-km.com</li>
        <li><svg viewBox="0 0 24 24"><circle cx="12" cy="12" r="10"/></svg>www.Tolbera-KM.com</li>
      </ul>
      <div class="rule"></div>
      <p class="address">480 Cedar Mill Road, Suite #210,<br>Brookfield, TX, United States, Texas</p>
    </div>
    <p class="tagline">The Most Trusted Assisted Living Communities</p>
  </section>

  <section class="card card--back" aria-label="Card back">
    <div class="wordmark">
      <div class="wordmark__name">Tolbera</div>
      <div class="wordmark__sub">LIVING</div>
    </div>
    <ul class="social" aria-label="Social media links">
      <li></li><li></li><li></li>
    </ul>
  </section>
</body>
</html>
```